Creative, Colorful, Dynamic Infographic for Global Non-Profit

We are a global arts and education non-profit in need of an infographic that illustrates four key skills embedded in our work: Curiosity, Listening, Imagination, Postive Action.
We work primarily with educators, students, and artists who use the power of personal stories to build community and connection and to bridge divides.
Our new brand guidelines, logos, and fonts are here: https://stylekit.example/quillbridge-7
I've attached a mock-up of the graphic and the required text. (Note the attached design was created by a staff person, your final design does not need to be the same. The color scheme and text of the final design should match the brand guidelines above.)
The graphic will be used for both web and print media and should include the purple Quillbridge 7 logo (also attached).
Ideally the final design will delight audiences and spark interest in our work.

```html
<!DOCTYPE html>
<html lang="en">
<head>
<meta charset="utf-8">
<title>Quillbridge 7 — Four Skills</title>
<link rel="stylesheet" href="https://fonts.googleapis.com/css2?family=Libre+Caslon+Text:wght@400;700&family=Outfit:wght@500;600&display=swap">
<style>
  :root {
    --purple: #663399;
    --purple-deep: #4a2470;
    --red: #ef4444;
    --red-deep: #b02c2c;
    --navy: #1f1d3d;
    --blue: #226cc4;
    --yellow: #e8c94a;
    --white: #ffffff;
    --shade: #d8d8d8;
    --icon-shade: #bdbdbd;
  }
  * { margin: 0; padding: 0; box-sizing: border-box; }
  html, body { width: 1200px; height: 800px; overflow: hidden; }
  body {
    position: relative;
    background: radial-gradient(ellipse at 50% 50%, #ffffff 0%, #f3f3f3 55%, #e1e1e1 100%);
    font-family: "Outfit", "Helvetica Neue", Arial, sans-serif;
  }
  .skills-wheel { position: absolute; inset: 0; width: 1200px; height: 800px; }
  .arc-text {
    font-family: "Outfit", "Helvetica Neue", Arial, sans-serif;
    font-weight: 500;
    font-size: 15.5px;
    letter-spacing: 0.3px;
    fill: var(--yellow);
  }
  .brand-name {
    font-family: "Outfit", "Helvetica Neue", Arial, sans-serif;
    font-weight: 600;
    font-size: 27px;
    fill: var(--navy);
  }
  .skill-title {
    position: absolute;
    width: 232px; height: 52px;
    padding: 4px 0 0 12px;
    font-family: "Libre Caslon Text", Georgia, serif;
    font-size: 33px;
    line-height: 44px;
    color: var(--white);
  }
  .skill-note {
    position: absolute;
    width: 232px; height: 71px;
    padding: 7px 12px 0 12px;
    background: var(--yellow);
    font-weight: 500;
    font-size: 14px;
    line-height: 18.4px;
    color: var(--navy);
  }
  .curiosity { background: var(--purple); }
  .positive-action { background: var(--red); }
  .listening { background: var(--navy); }
  .imagination { background: var(--blue); }
  .left { left: 61px; }
  .right { left: 908px; }
</style>
</head>
<body>

<svg class="skills-wheel" viewBox="0 0 1200 800" xmlns="http://www.w3.org/2000/svg" aria-hidden="false">
  <defs>
    <path id="arc-curiosity" d="M 382,400 A 218 218 0 0 1 600,182"/>
    <path id="arc-action-outer" d="M 600,168 A 232 232 0 0 1 832,400"/>
    <path id="arc-action-inner" d="M 600,192 A 208 208 0 0 1 808,400"/>
    <path id="arc-listen-inner" d="M 400,400 A 200 200 0 0 0 600,600"/>
    <path id="arc-listen-outer" d="M 376,400 A 224 224 0 0 0 600,624"/>
    <path id="arc-imagine-inner" d="M 600,600 A 200 200 0 0 0 800,400"/>
    <path id="arc-imagine-outer" d="M 600,624 A 224 224 0 0 0 824,400"/>
  </defs>

  <!-- connectors -->
  <g class="connectors" fill="none" stroke-width="2" stroke-dasharray="8 5">
    <path d="M 240,213 V 124 H 455" stroke="var(--purple)"/>
    <path d="M 745,124 H 961 V 213" stroke="var(--red)"/>
    <path d="M 247,656 V 687 H 455" stroke="var(--navy)"/>
    <path d="M 745,687 H 956 V 656" stroke="var(--blue)"/>
  </g>

  <!-- ring shadow -->
  <circle cx="612" cy="412" r="284" fill="var(--shade)"/>
  <circle cx="607" cy="407" r="147" fill="var(--white)"/>

  <!-- ring segments -->
  <g class="ring">
    <path class="segment-curiosity" fill="var(--purple)"
      d="M 323,398 A 277 277 0 0 1 596,123 L 596,158 L 572,182 L 596,206 L 596,241 A 159 159 0 0 0 441,398 L 400,398 L 382,416 L 364,398 Z"/>
    <path class="segment-action" fill="var(--red)"
      d="M 604,123 A 277 277 0 0 1 877,394 L 842,394 L 818,370 L 794,394 L 759,394 A 159 159 0 0 0 604,241 L 604,200 L 586,182 L 604,164 Z"/>
    <path class="segment-imagination" fill="var(--blue)"
      d="M 877,406 A 277 277 0 0 1 604,677 L 604,642 L 628,618 L 604,594 L 604,559 A 159 159 0 0 0 759,406 L 800,406 L 818,388 L 836,406 Z"/>
    <path class="segment-listening" fill="var(--navy)"
      d="M 596,677 A 277 277 0 0 1 323,406 L 358,406 L 382,430 L 406,406 L 441,406 A 159 159 0 0 0 596,559 L 596,600 L 614,618 L 596,636 Z"/>
  </g>

  <!-- ring captions -->
  <text class="arc-text"><textPath href="#arc-curiosity" startOffset="50%" text-anchor="middle">Your curiosity allows you to listen</textPath></text>
  <text class="arc-text"><textPath href="#arc-action-outer" startOffset="52%" text-anchor="middle">Your positive actions lead to</textPath></text>
  <text class="arc-text"><textPath href="#arc-action-inner" startOffset="54%" text-anchor="middle">curiosity about what else is possible</textPath></text>
  <text class="arc-text"><textPath href="#arc-listen-inner" startOffset="54%" text-anchor="middle">Your listening allows you to take</textPath></text>
  <text class="arc-text"><textPath href="#arc-listen-outer" startOffset="42%" text-anchor="middle">in new information</textPath></text>
  <text class="arc-text"><textPath href="#arc-imagine-inner" startOffset="52%" text-anchor="middle">Your imagination can spark</textPath></text>
  <text class="arc-text"><textPath href="#arc-imagine-outer" startOffset="50%" text-anchor="middle">positive action</textPath></text>

  <!-- brand name -->
  <text class="brand-name" x="600" y="409" text-anchor="middle">Quillbridge 7</text>

  <!-- icon badges -->
  <g class="badge badge-curiosity" transform="translate(485,124)">
    <circle cx="7" cy="7" r="43" fill="var(--icon-shade)"/>
    <circle r="43" fill="var(--white)"/>
    <circle cx="5" cy="5" r="30" fill="var(--purple-deep)"/>
    <circle r="30" fill="var(--purple)"/>
    <circle cx="-3" cy="-3" r="11" fill="none" stroke="var(--white)" stroke-width="2.5"/>
    <line x1="5" y1="5" x2="14" y2="14" stroke="var(--white)" stroke-width="3" stroke-linecap="round"/>
    <text x="-3" y="1.5" text-anchor="middle" font-family="Outfit, sans-serif" font-weight="600" font-size="12" fill="var(--white)">?</text>
  </g>

  <g class="badge badge-action" transform="translate(717,122)">
    <circle cx="7" cy="7" r="43" fill="var(--icon-shade)"/>
    <circle r="43" fill="var(--white)"/>
    <circle cx="5" cy="5" r="30" fill="var(--red-deep)"/>
    <circle r="30" fill="var(--red)"/>
    <circle cx="4" cy="-8" r="6.5" fill="var(--white)"/>
    <path d="M 1,-8 L 3.5,-5.5 L 7.5,-10.5" fill="none" stroke="var(--red)" stroke-width="1.8" stroke-linecap="round" stroke-linejoin="round"/>
    <path d="M -16,6 H -10 Q -3,1 5,4 H 9 Q 12,4 10,7 L 16,4 Q 19,4 16,8 L 8,13 H -16 Z" fill="var(--white)"/>
  </g>

  <g class="badge badge-listening" transform="translate(486,670)">
    <circle cx="7" cy="7" r="43" fill="var(--icon-shade)"/>
    <circle r="43" fill="var(--white)"/>
    <circle r="30" fill="var(--navy)"/>
    <ellipse cx="0" cy="-7" rx="6.5" ry="8" fill="var(--white)"/>
    <path d="M -14,15 Q -14,3 0,3 Q 14,3 14,15 Z" fill="var(--white)"/>
    <path d="M -11,-11 Q -14,-7 -11,-3 M -15,-13 Q -19,-7 -15,-1" fill="none" stroke="var(--white)" stroke-width="1.3" stroke-linecap="round"/>
    <path d="M 11,-11 Q 14,-7 11,-3 M 15,-13 Q 19,-7 15,-1" fill="none" stroke="var(--white)" stroke-width="1.3" stroke-linecap="round"/>
  </g>

  <g class="badge badge-imagination" transform="translate(716,669)">
    <circle cx="7" cy="7" r="43" fill="var(--icon-shade)"/>
    <circle r="43" fill="var(--white)"/>
    <circle r="30" fill="var(--blue)"/>
    <circle cx="0" cy="-3" r="8.5" fill="var(--white)"/>
    <rect x="-4.5" y="4" width="9" height="7" rx="1" fill="var(--white)"/>
    <rect x="-3" y="12" width="6" height="2.5" rx="1" fill="var(--white)"/>
    <path d="M 0,-17 V -15 M -9,-14 L -8,-12.5 M 9,-14 L 8,-12.5" stroke="var(--white)" stroke-width="1.5" stroke-linecap="round"/>
  </g>
</svg>

<div class="skill-title curiosity left" style="top:213px;">Curiosity</div>
<div class="skill-note left" style="top:273px;">Focus on how you can learn from another’s knowledge and experience</div>

<div class="skill-title positive-action right" style="top:213px;">Positive action</div>
<div class="skill-note right" style="top:273px;">Show your words and actions matter</div>

<div class="skill-note left" style="top:524px;">Seek to understand before speaking</div>
<div class="skill-title listening left" style="top:604px;">Listening</div>

<div class="skill-note right" style="top:524px;">Consider possibilities beyond what you know</div>
<div class="skill-title imagination right" style="top:604px;">Imagination</div>

</body>
</html>
```